Business Card for Jewelry Business

We need a new namecard design for a jewelry company based in Bangkok, Thailand. We have a new website recently and want the new namecard to reflect our new modern image. I have uploaded our old namecard to show you the information that needs to be on the namecard. Pls check our website www.qelburn.com for the new color scheme to help design the new namecard.

```html
<!DOCTYPE html>
<html lang="en">
<head>
<meta charset="utf-8">
<title>Qelburn Makers – Business Card</title>
<link rel="stylesheet" href="https://fonts.googleapis.com/css2?family=Roboto:wght@400;500;700&display=swap">
<style>
  :root {
    --bg: #dcdcdc;
    --teal: #52c4c9;
    --sand: #e6ddd3;
    --ink: #1f1f1f;
    --card-dark: #232323;
    --white: #ffffff;
  }
  * { box-sizing: border-box; margin: 0; padding: 0; }
  html, body { width: 1200px; height: 1059px; overflow: hidden; }
  body {
    background: var(--bg);
    font-family: "Roboto", Arial, sans-serif;
    color: var(--ink);
    position: relative;
  }
  .card {
    position: absolute;
    left: 255px;
    width: 690px;
    height: 392px;
    border-radius: 20px;
    overflow: hidden;
  }
  .card--front { top: 100px; background: var(--white); }
  .card--back { top: 538px; background: var(--card-dark); }

  .brand {
    position: absolute;
    display: flex;
    align-items: center;
    gap: 12px;
  }
  .brand__dot { border-radius: 50%; background: var(--teal); flex: none; }
  .brand__text { font-weight: 400; text-align: center; line-height: 1.1; }
  .brand__name { display: block; letter-spacing: 1px; }
  .brand__sub { display: block; letter-spacing: 1.5px; }

  .card--front .brand { right: 32px; top: 68px; }
  .card--front .brand__dot { width: 34px; height: 34px; }
  .card--front .brand__text { color: var(--ink); }
  .card--front .brand__name { font-size: 24px; }
  .card--front .brand__sub { font-size: 9px; margin-top: 8px; }

  .person { position: absolute; left: 29px; top: 170px; }
  .person__name { font-size: 24px; font-weight: 700; color: var(--teal); letter-spacing: 0.3px; }
  .person__role { font-size: 16.5px; margin-top: 4px; }

  .divider {
    position: absolute; left: 29px; right: 29px; top: 236px;
    height: 1px; background: var(--sand);
  }

  .contacts { position: absolute; left: 29px; top: 254px; list-style: none; }
  .contacts li { display: flex; align-items: center; gap: 6px; font-size: 16px; height: 22.5px; }
  .contacts svg { width: 12px; height: 12px; fill: var(--teal); flex: none; }

  .address {
    position: absolute; right: 29px; top: 256px;
    text-align: right; font-size: 16px; line-height: 22px; font-style: normal;
  }

  .band { position: absolute; left: 0; bottom: 0; width: 100%; height: 11px; }

  .card--back .brand { left: 50%; top: 140px; transform: translateX(-50%); gap: 18px; }
  .card--back .brand__dot { width: 56px; height: 56px; }
  .card--back .brand__text { color: var(--white); }
  .card--back .brand__name { font-size: 38px; }
  .card--back .brand__sub { font-size: 13px; margin-top: 12px; letter-spacing: 2px; }

  .socials {
    position: absolute; left: 0; right: 0; top: 348px;
    display: flex; justify-content: center; gap: 16px;
    color: var(--white); font-size: 16.5px;
  }
  .socials span { display: flex; align-items: center; gap: 6px; }
  .socials__circle { width: 13px; height: 13px; border-radius: 50%; background: var(--teal); }
  .socials__square { width: 13px; height: 13px; border: 2px solid var(--teal); border-radius: 3px; }
</style>
</head>
<body>

<section class="card card--front">
  <div class="brand">
    <span class="brand__dot"></span>
    <span class="brand__text">
      <span class="brand__name">QELBURN</span>
      <span class="brand__sub">MAKERS</span>
    </span>
  </div>

  <div class="person">
    <h1 class="person__name">NALIN SUPACHAI</h1>
    <p class="person__role">Sales &amp; Product Development Manager</p>
  </div>

  <div class="divider"></div>

  <ul class="contacts">
    <li><svg viewBox="0 0 24 24"><path d="M6.6 10.8a15.1 15.1 0 0 0 6.6 6.6l2.2-2.2c.3-.3.7-.4 1-.2 1.1.4 2.3.6 3.6.6.6 0 1 .4 1 1V20c0 .6-.4 1-1 1C10.6 21 3 13.4 3 4c0-.6.4-1 1-1h3.5c.6 0 1 .4 1 1 0 1.3.2 2.5.6 3.6.1.3 0 .7-.2 1z"/></svg>+662-418-5530-2</li>
    <li><svg viewBox="0 0 24 24"><path d="M6 2h12v5H6zM4 8h16a2 2 0 0 1 2 2v7h-4v5H6v-5H2v-7a2 2 0 0 1 2-2zm4 8v4h8v-4z"/></svg>+662-580-2194</li>
    <li><svg viewBox="0 0 24 24"><path d="M2 5h20v14H2zm2 2v.4l8 5.4 8-5.4V7z"/></svg>nalin@qelburn.com</li>
    <li><svg viewBox="0 0 24 24"><path d="M2 5h20v14H2zm2 2v.4l8 5.4 8-5.4V7z"/></svg>hello@qelburn.com</li>
    <li><svg viewBox="0 0 24 24"><path d="M12 2a10 10 0 1 0 0 20 10 10 0 0 0 0-20zm-1 17.9A8 8 0 0 1 4.2 10.8L9 15.6v1a2 2 0 0 0 2 2zm6.9-2.5A2 2 0 0 0 16 16h-1v-3a1 1 0 0 0-1-1H8v-2h2a1 1 0 0 0 1-1V7h2a2 2 0 0 0 2-2v-.4a8 8 0 0 1 2.9 12.8z"/></svg>www.qelburn.com</li>
  </ul>

  <address class="address">
    Qelburn Makers Co.,Ltd.<br>
    128 Moo 7 Sukprasert Road<br>
    Export Processing Zone 5,<br>
    Rimnam Industrial Estate,<br>
    Rimnam, Bangkok 10990 Thailand
  </address>

  <svg class="band" viewBox="0 0 690 11" preserveAspectRatio="none" aria-hidden="true">
    <rect x="0" y="0" width="690" height="11" fill="var(--sand)"/>
    <polygon points="0,0 352,0 336,11 0,11" fill="var(--teal)"/>
  </svg>
</section>

<section class="card card--back">
  <div class="brand">
    <span class="brand__dot"></span>
    <span class="brand__text">
      <span class="brand__name">QELBURN</span>
      <span class="brand__sub">MAKERS</span>
    </span>
  </div>

  <div class="socials">
    <span><i class="socials__circle"></i>Qelburn Makers</span>
    <span><i class="socials__square"></i>@QelburnMk</span>
  </div>
</section>

</body>
</html>
```